Modern card design needed for building development company

We are looking for a sharp modern new look for our business cards.
We are a New Zealand based company called TKV Ventures NZ LTD that specialises in subdividing large sections, housing and commercial buildings.
We have attached a photo of the current logo and would like to see it improved somehow as it looks a bit dated.
We are open to any colours.

Target Market(s)

Investors, Property buyers

Industry/Entity Type

Investment

Contact Information for Business Card

TKV VENTURES NZ LTD
www.tkvventuresnz.co.nz

Howard Pennick
Phone +64 21 843 192
Email hdpennick@fernmail.co.nz

Font styles to use
Serif
Sans Serif

Colors
0792cd
33a6d7
85cae6
6b449b
886aae
f04a50
ec1f27
f37122
f68d4d

Requirements
Must have
• Please try and make the logo more modern or if you have a similar one we would like to see it.

```html
<!DOCTYPE html>
<html lang="en">
<head>
<meta charset="utf-8">
<title>TKV Ventures NZ LTD – Business Card</title>
<link rel="stylesheet" href="https://fonts.googleapis.com/css2?family=Anton&family=Michroma&family=Montserrat:wght@700&family=Open+Sans:wght@400&display=swap">
<style>
  :root {
    --page-bg: #ececee;
    --card-deep: #06052b;
    --card-mid: #0d0b3c;
    --card-glow: #1c1a55;
    --brand-blue: #1b7fc6;
    --brand-sky: #2aa8e0;
    --text-light: #ffffff;
    --shadow: rgba(0, 0, 0, 0.28);
  }
  * { box-sizing: border-box; margin: 0; padding: 0; }
  html, body {
    width: 1200px;
    height: 1200px;
    overflow: hidden;
    background: var(--page-bg);
  }
  .sheet {
    position: relative;
    width: 1200px;
    height: 1200px;
    display: flex;
    flex-direction: column;
    align-items: center;
    justify-content: center;
    gap: 60px;
  }
  .card {
    position: relative;
    width: 880px;
    height: 503px;
    overflow: hidden;
    background:
      radial-gradient(ellipse 45% 40% at 22% 55%, var(--card-glow) 0%, transparent 70%),
      radial-gradient(ellipse 40% 35% at 75% 25%, #15134a 0%, transparent 70%),
      linear-gradient(160deg, var(--card-mid) 0%, var(--card-deep) 100%);
    box-shadow: 6px 8px 14px var(--shadow);
  }

  /* Front */
  .card--front .brand {
    position: absolute;
    left: 0; right: 0;
    top: 170px;
    display: flex;
    align-items: center;
    justify-content: center;
    gap: 22px;
  }
  .brand__square {
    width: 74px;
    height: 74px;
    background: var(--brand-blue);
  }
  .brand__name {
    font-family: "Michroma", sans-serif;
    font-size: 26px;
    letter-spacing: 1px;
    color: var(--brand-blue);
  }
  .card--front .website {
    position: absolute;
    left: 0; right: 0;
    top: 320px;
    text-align: center;
    font-family: "Montserrat", sans-serif;
    font-weight: 700;
    font-size: 26px;
    letter-spacing: 0.5px;
    color: var(--text-light);
  }

  /* Back */
  .card--back .brand {
    position: absolute;
    left: 230px;
    top: 300px;
    display: flex;
    flex-direction: column;
    align-items: flex-start;
    gap: 22px;
  }
  .card--back .brand__square {
    width: 86px;
    height: 86px;
    background: var(--brand-sky);
  }
  .card--back .brand__name {
    font-size: 22px;
    color: var(--text-light);
  }
  .contact {
    position: absolute;
    right: 70px;
    top: 120px;
    text-align: left;
    color: var(--text-light);
  }
  .contact__name {
    font-family: "Anton", sans-serif;
    font-size: 40px;
    line-height: 1.1;
    letter-spacing: 0.5px;
    margin-bottom: 14px;
  }
  .contact__line {
    display: flex;
    align-items: center;
    gap: 12px;
    font-family: "Open Sans", sans-serif;
    font-size: 19px;
    line-height: 1.9;
  }
  .contact__icon { width: 20px; height: 20px; flex: none; }
</style>
</head>
<body>
<main class="sheet">

  <section class="card card--front" aria-label="Card front">
    <div class="brand">
      <span class="brand__square"></span>
      <span class="brand__name">TKV VENTURES NZ LTD</span>
    </div>
    <p class="website">www.tkvventuresnz.co.nz</p>
  </section>

  <section class="card card--back" aria-label="Card back">
    <div class="contact">
      <h1 class="contact__name">Howard Pennick</h1>
      <p class="contact__line">
        <svg class="contact__icon" viewBox="0 0 20 20" aria-hidden="true">
          <rect x="5" y="1.5" width="10" height="17" rx="2" fill="none" stroke="#2aa8e0" stroke-width="2"/>
          <circle cx="10" cy="15" r="1.2" fill="#2aa8e0"/>
        </svg>
        +64 21 843 192
      </p>
      <p class="contact__line">
        <svg class="contact__icon" viewBox="0 0 20 20" aria-hidden="true">
          <rect x="1" y="4" width="18" height="12" fill="#2aa8e0"/>
          <path d="M1 4 L10 11 L19 4" fill="none" stroke="#0d0b3c" stroke-width="1.5"/>
        </svg>
        hdpennick@fernmail.co.nz
      </p>
    </div>
    <div class="brand">
      <span class="brand__square"></span>
      <span class="brand__name">TKV VENTURES NZ LTD</span>
    </div>
  </section>

</main>
</body>
</html>
```